Interior Logo Posters

We want 4 posters for the inside of our business. We need them full resolution so we can blow them up. We have 4 stock photos and want our logo put in various locations.

Industry/Entity Type

Business

```html
<!DOCTYPE html>
<html lang="en">
<head>
<meta charset="utf-8">
<title>KorvanAuto Interior Posters</title>
<link rel="stylesheet" href="https://fonts.googleapis.com/css2?family=Montserrat:wght@600&family=Raleway:wght@400&display=swap">
<style>
  :root {
    --page: #ffffff;
    --board: #bbbcc1;
    --ink-dark: #2e2e30;
    --ink-light: #ffffff;
    --wordmark: #ffffff;
    --accent: #e0463a;
    --shade: #050505;
  }
  * { margin: 0; padding: 0; box-sizing: border-box; }
  html, body { width: 1200px; height: 1200px; overflow: hidden; background: var(--page); }
  .board {
    position: absolute; left: 59px; top: 57px; width: 1087px; height: 1086px;
    background: var(--board);
  }
  .poster {
    position: absolute; width: 471px; height: 314px; overflow: hidden;
  }
  .poster--driver { left: 51px; top: 69px; }
  .poster--dash { left: 567px; top: 69px; }
  .poster--mirror { left: 51px; top: 537px; }
  .poster--city { left: 567px; top: 539px; height: 312px; }

  .poster__photo { position: absolute; inset: 0; }
  .poster--driver .poster__photo {
    background: radial-gradient(ellipse at 70% 30%, #f1e7c4 0%, #c98d3a 28%, #5a3a18 55%, #120a04 85%);
  }
  .poster--dash .poster__photo {
    background: radial-gradient(ellipse at 75% 35%, #4a3a40 0%, #1d1f26 40%, #0a0b0e 80%);
  }
  .poster--mirror .poster__photo {
    background: linear-gradient(170deg, #e8dc8a 0%, #8fa14a 22%, #4f6b35 42%, #5a5d5c 62%, #2b2e30 82%, #1a1c1e 100%);
  }
  .poster--city .poster__photo {
    background: linear-gradient(180deg, #4d6274 0%, #2d3d4a 35%, #2a3138 60%, #6d6a6a 80%, #1c2024 100%);
  }
  .poster__shade {
    position: absolute; inset: 0;
    background: radial-gradient(ellipse 70% 60% at 85% 95%, rgba(5,5,5,0.95) 0%, rgba(5,5,5,0.7) 45%, rgba(5,5,5,0) 100%);
  }
  .brand {
    position: absolute; left: 289px; top: 222px; width: 140px;
    display: flex; flex-direction: column; align-items: center; gap: 11px;
  }
  .brand__mark { width: 28px; height: 28px; background: var(--accent); }
  .brand__name {
    font-family: "Montserrat", sans-serif; font-weight: 600; font-size: 10.5px;
    letter-spacing: 4.6px; margin-right: -4.6px; color: var(--wordmark); white-space: nowrap;
  }
  .caption {
    position: absolute; left: 0; top: 980px; width: 1087px; text-align: center;
    font-family: "Raleway", sans-serif; font-size: 23px; line-height: 32px;
  }
  .caption__line--dark { color: var(--ink-dark); }
  .caption__line--light { color: var(--ink-light); }
</style>
</head>
<body>
  <main class="board">
    <section class="poster poster--driver">
      <div class="poster__photo" role="img" aria-label="Driver seen from the back seat, steering in warm golden sunset light through the windscreen"></div>
      <div class="poster__shade"></div>
      <div class="brand"><span class="brand__mark"></span><span class="brand__name">KORVANAUTO</span></div>
    </section>
    <section class="poster poster--dash">
      <div class="poster__photo" role="img" aria-label="Close view of a dark steering wheel and illuminated dashboard gauges with red accents"></div>
      <div class="poster__shade"></div>
      <div class="brand"><span class="brand__mark"></span><span class="brand__name">KORVANAUTO</span></div>
    </section>
    <section class="poster poster--mirror">
      <div class="poster__photo" role="img" aria-label="Side mirror of a moving car with motion-blurred green trees and red railing"></div>
      <div class="poster__shade"></div>
      <div class="brand"><span class="brand__mark"></span><span class="brand__name">KORVANAUTO</span></div>
    </section>
    <section class="poster poster--city">
      <div class="poster__photo" role="img" aria-label="City road at dusk with light trails from traffic, street lamps and tall buildings"></div>
      <div class="poster__shade"></div>
      <div class="brand"><span class="brand__mark"></span><span class="brand__name">KORVANAUTO</span></div>
    </section>
    <p class="caption">
      <span class="caption__line--dark">KA logo positioned on lower right of each poster on top of a blurred black area.</span><br>
      <span class="caption__line--light">Poster art set at large US poster size: 36"X 24" at 300dpi This can be scaled up.</span>
    </p>
  </main>
</body>
</html>
```